edgy fitness flyer

Utilize quote
"I don't want a great body"
by: Nobody Ever
Offer oin back . Vard needs to be edgy and sexy.

Target Market(s)

Women and men 25-45

Industry/Entity Type

Fitness

Requirements
Must have
• clear font layered over gradient image
• See attached sample.
• bright and eye catching
• must coordniate with studio image
• www.plovarfitness.com

```html
<!DOCTYPE html>
<html lang="en">
<head>
<meta charset="utf-8">
<title>Plovar Fitness – I Dont want a Great Body</title>
<link rel="stylesheet" href="https://fonts.googleapis.com/css2?family=Arvo:wght@400;700&display=swap">
<style>
  :root {
    --magenta: #d4127e;
    --magenta-deep: #7a0748;
    --magenta-dark: #3d0326;
    --ink: #0d0a0c;
    --silver-top: #ffffff;
    --silver-bottom: #bfbfbf;
    --orange: #f4a13a;
    --logo-orange: #f7941d;
    --cyan: #2bb8ea;
    --white: #ffffff;
    --band: rgba(25, 6, 18, 0.82);
    --logo-panel: rgba(240, 70, 150, 0.45);
  }
  html, body {
    margin: 0;
    padding: 0;
    overflow: hidden;
    background: #222;
  }
  .flyer {
    position: relative;
    width: 845px;
    height: 1200px;
    overflow: hidden;
    font-family: "Arvo", Georgia, serif;
    background:
      radial-gradient(ellipse at 55% 55%, var(--magenta) 0%, #b50f6c 45%, var(--magenta-deep) 80%, var(--magenta-dark) 100%);
  }
  .flyer__grunge {
    position: absolute;
    inset: 0;
    background: linear-gradient(180deg, rgba(60,0,30,0.55) 0%, rgba(60,0,30,0) 30%, rgba(60,0,30,0) 75%, rgba(40,0,20,0.5) 100%);
  }
  .headline-splash {
    position: absolute;
    left: 150px;
    top: 20px;
    width: 560px;
    height: 330px;
    border-radius: 46% 40% 44% 50% / 50% 46% 54% 50%;
    background: radial-gradient(ellipse at center, #0b0b0b 0%, #141014 55%, rgba(20,10,16,0.85) 75%, rgba(20,10,16,0) 100%);
  }
  .headline {
    position: absolute;
    left: 0;
    top: 112px;
    width: 845px;
    margin: 0;
    text-align: center;
    font-weight: 700;
    font-size: 64px;
    line-height: 74px;
    background: linear-gradient(180deg, var(--silver-top) 0%, #e8e8e8 50%, var(--silver-bottom) 100%);
    -webkit-background-clip: text;
    background-clip: text;
    color: transparent;
    filter: drop-shadow(2px 3px 2px rgba(0,0,0,0.8));
  }
  .byline {
    position: absolute;
    left: 0;
    top: 272px;
    width: 845px;
    margin: 0;
    text-align: center;
    font-weight: 700;
    font-size: 45px;
    color: var(--orange);
    text-shadow: 2px 2px 2px rgba(0,0,0,0.7);
  }
  .figure {
    position: absolute;
    left: 470px;
    top: 345px;
    width: 375px;
    height: 855px;
    border-radius: 45% 20% 0 40% / 25% 10% 0 30%;
    background: linear-gradient(160deg, #1a0c14 0%, #0a0608 60%, #050304 100%);
  }
  .brand-panel {
    position: absolute;
    left: 0;
    top: 588px;
    width: 336px;
    height: 132px;
    background: var(--logo-panel);
    display: flex;
    align-items: center;
    padding-left: 30px;
    box-sizing: border-box;
    gap: 14px;
  }
  .brand-panel__mark {
    width: 22px;
    height: 22px;
    background: var(--logo-orange);
  }
  .brand-panel__name {
    font-weight: 700;
    font-size: 44px;
    color: var(--logo-orange);
    letter-spacing: 1px;
  }
  .band {
    position: absolute;
    background: var(--band);
    transform-origin: left center;
    transform: rotate(-11deg);
    color: var(--cyan);
    font-weight: 700;
    box-sizing: border-box;
  }
  .band__title {
    display: block;
    font-size: 40px;
    line-height: 46px;
    text-shadow: 1px 1px 0 rgba(0,0,0,0.6);
  }
  .band__sub {
    display: block;
    color: var(--white);
    font-size: 19px;
    line-height: 24px;
    padding-left: 62px;
  }
  .band--stats {
    left: -10px;
    top: 820px;
    width: 620px;
    height: 110px;
    padding: 8px 0 0 22px;
    text-align: center;
  }
  .band--ego {
    left: 168px;
    top: 935px;
    width: 700px;
    height: 88px;
    padding: 6px 0 0 10px;
  }
  .band--dirty {
    left: 212px;
    top: 1045px;
    width: 520px;
    height: 84px;
    padding: 4px 0 0 10px;
  }
  .band--dirty .band__sub { padding-left: 28px; }
</style>
</head>
<body>
  <main class="flyer">
    <div class="flyer__grunge" role="img" aria-label="Grunge scratched texture over magenta background"></div>
    <div class="headline-splash" role="img" aria-label="Black ink splatter with faint red ornament behind the headline"></div>

    <h1 class="headline">I Dont want a<br>Great Body</h1>
    <p class="byline">By: Nobody Ever</p>

    <div class="figure" role="img" aria-label="Black silhouette of a woman with a hand raised to her head and a pink highlight along her hair and back"></div>

    <div class="brand-panel">
      <span class="brand-panel__mark"></span>
      <span class="brand-panel__name">Plovar Fitness</span>
    </div>

    <div class="band band--stats">
      <span class="band__title">40 Minutes.700 Calories<br>21 Days</span>
    </div>

    <div class="band band--ego">
      <span class="band__title">Check Your EGO at the door.</span>
      <span class="band__sub">Complete, Dont Compete.</span>
    </div>

    <div class="band band--dirty">
      <span class="band__title">Get Down.Get Dirty</span>
      <span class="band__sub">Get in the best shape of your life</span>
    </div>
  </main>
</body>
</html>
```